Web Design Project

blaze guard safety & solutions needs a new web design to go with its new logo design

we provide services such as instillation of fire sprinklers, fire hydrants , fire hose reels as well as fire extinguishers and fire blankets.

we can service these as well and also do the preventitave maintaince of these too.

we can do flow testing of sprinklers,hydrants & hosereels and test back flow prevention devices as well

old page is bgss-example.com.au

Industry/Entity Type

Defence

```html
<!DOCTYPE html>
<html lang="en">
<head>
<meta charset="utf-8">
<title>Blaze Guard Safety &amp; Solutions</title>
<link href="https://fonts.googleapis.com/css2?family=Ubuntu:wght@400;500;700&family=Arimo:wght@400;700&display=swap" rel="stylesheet">
<style>
:root{
  --red:#c8111a;
  --red-dark:#5c0a10;
  --red-mid:#9a0d16;
  --nav:#4a4a4a;
  --nav-dark:#333;
  --grey-bg:#e6e6e6;
  --footer:#dcdcdc;
  --text:#444;
  --blue:#13a3d8;
  --white:#fff;
}
*{box-sizing:border-box;margin:0;padding:0}
html,body{width:1183px;height:1200px;overflow:hidden;background:var(--grey-bg)}
body{font-family:"Arimo",Arial,sans-serif;color:var(--text)}
.page{position:absolute;top:0;left:0;width:1200px;height:1217px;transform:scale(.98583);transform-origin:0 0;
  background:linear-gradient(#fff 728px,#f4f4f4 900px,#fff 1124px,var(--footer) 1124px)}
.top-band{position:absolute;top:0;left:0;width:1200px;height:728px;
  background:radial-gradient(ellipse at 50% 0%,#b3121c 0%,var(--red-mid) 40%,var(--red-dark) 100%)}
.abs{position:absolute}
.brand{left:118px;top:18px;display:flex;align-items:center;gap:14px}
.brand-mark{width:44px;height:44px;background:var(--red);border:3px solid #fff}
.brand-name{font-family:"Ubuntu",sans-serif;font-weight:500;color:#fff;font-size:24px;line-height:28px;letter-spacing:2px;text-transform:uppercase}
.contact-link{right:115px;top:12px;color:#fff;font-family:"Ubuntu",sans-serif;font-size:13px;font-weight:500;display:flex;align-items:center;gap:7px}
.search{left:857px;top:51px;width:228px;height:27px;display:flex;border-radius:4px;overflow:hidden;border:1px solid #aaa}
.search-field{flex:1;background:#fff;display:flex;align-items:center;gap:6px;padding-left:6px;font-size:11px;color:#999}
.search-btn{width:63px;background:linear-gradient(#e5232c,#b10d15);color:#fff;font-family:"Ubuntu",sans-serif;font-size:13px;display:flex;align-items:center;justify-content:center}
.nav{left:115px;top:107px;width:970px;height:50px;background:linear-gradient(#5a5a5a,var(--nav-dark));border-radius:4px 4px 0 0;
  display:flex;align-items:flex-end;padding-left:17px;font-family:"Ubuntu",sans-serif;font-size:16px;color:#ddd}
.nav-item{height:42px;padding:0 15px;display:flex;align-items:center;gap:5px;margin-right:14px}
.nav-item.active{background:#fff;color:#333;border-radius:3px 3px 0 0}
.nav-phone{margin-left:auto;margin-right:16px;height:50px;display:flex;align-items:center;gap:8px;color:#fff;font-weight:500}
.hero-frame{left:115px;top:157px;width:970px;height:397px;background:#fff;border-radius:0 0 4px 4px;box-shadow:0 6px 12px rgba(0,0,0,.35)}
.hero{left:125px;top:166px;width:951px;height:378px;border-radius:4px;overflow:hidden;
  background:linear-gradient(90deg,#2b2622 0%,#3d3327 32%,#8a6a1c 50%,#c98a1a 62%,#e2621a 78%,#6b5440 100%)}
.hero-title{left:140px;top:190px;color:#f2f2f2;font-family:"Ubuntu",sans-serif;font-size:74px;font-weight:400;letter-spacing:-3px;line-height:80px}
.hero-sub{left:146px;top:266px;color:#eee;font-family:"Ubuntu",sans-serif;font-size:40px;letter-spacing:-1.5px}
.hero-lead{left:142px;top:320px;width:340px;font-family:"Ubuntu",sans-serif;font-size:18px;line-height:23px;color:#fff}
.hero-lead span{background:var(--red);padding:0 5px;box-decoration-break:clone;-webkit-box-decoration-break:clone}
.hero-btn{left:144px;top:464px;width:228px;height:55px;border-radius:4px;background:linear-gradient(#e8262f,#a90b13);
  color:#fff;font-family:"Ubuntu",sans-serif;font-size:22px;display:flex;align-items:center;padding-left:15px;gap:22px;box-shadow:0 2px 4px rgba(0,0,0,.4)}
.thumbs{left:828px;top:486px;display:flex;gap:6px}
.thumb{width:53px;height:48px;border:2px solid #fff;border-radius:4px}
.stats{left:115px;top:574px;width:970px;height:168px;background:#fff;border-radius:4px;box-shadow:0 4px 8px rgba(0,0,0,.2);display:flex;padding:12px 0}
.stat{flex:1;border-right:1px solid #e4e4e4;text-align:center;font-family:"Ubuntu",sans-serif;position:relative}
.stat:last-child{border-right:none}
.stat-title{position:absolute;left:0;right:0;top:98px;font-size:13px;font-weight:500;color:#333}
.stat-note{position:absolute;left:8px;right:8px;top:118px;font-size:11px;line-height:13px;color:#555}
.big-48{position:absolute;left:0;right:0;top:8px;font-size:80px;font-weight:700;line-height:80px;letter-spacing:-2px;
  color:#ddd;-webkit-text-stroke:1px #aaa;text-shadow:0 3px 3px rgba(0,0,0,.15)}
.million{position:absolute;left:0;right:0;top:28px;font-size:34px;font-weight:700;color:var(--blue);letter-spacing:-1px;line-height:34px}
.million small{display:block;font-size:14px;color:#111;letter-spacing:-.3px;line-height:14px;margin-top:-4px}
.exit-sign{position:absolute;left:64px;top:20px}
.hand-truck{position:absolute;left:72px;top:8px;width:84px;height:90px;background:linear-gradient(#eee,#c9b08a);border-radius:4px}
.welcome{left:117px;top:764px;font-family:"Ubuntu",sans-serif;font-weight:500;font-size:31px;color:var(--red)}
.intro{left:117px;top:808px;width:680px;font-family:"Ubuntu",sans-serif;font-weight:500;font-size:14.4px;line-height:19px;letter-spacing:-.2px;color:var(--blue)}
.body-copy{left:117px;top:862px;width:655px;font-size:12px;line-height:19px;color:#555}
.body-copy p{margin-bottom:19px}
.divider{left:778px;top:760px;width:1px;height:360px;background:linear-gradient(#fff,#ddd,#fff)}
.quote{left:791px;top:758px;width:295px;height:161px;border-radius:5px;background:linear-gradient(135deg,#d71a22,#a50d15);color:#fff;font-family:"Ubuntu",sans-serif;box-shadow:0 3px 6px rgba(0,0,0,.25)}
.quote-small{position:absolute;left:14px;top:12px;font-size:20px}
.quote-big{position:absolute;left:13px;top:32px;font-size:42px;font-weight:500}
.quote-note{position:absolute;left:13px;top:90px;width:215px;font-size:11px;font-weight:700;line-height:14px}
.quote-bubble{position:absolute;right:4px;top:2px}
.product{left:791px;top:927px;width:295px;height:158px;border-radius:5px;background:linear-gradient(#fff,#e6e6e6);border:1px solid #d8d8d8;box-shadow:0 3px 6px rgba(0,0,0,.2)}
.product-img{position:absolute;left:14px;top:20px;width:92px;height:116px;background:linear-gradient(135deg,#2b49a6,#e9e9f2 60%,#f1d23a)}
.product-title{position:absolute;left:122px;top:14px;font-family:"Ubuntu",sans-serif;font-weight:500;font-size:18px;line-height:19px;color:var(--red)}
.product-text{position:absolute;left:123px;top:60px;width:165px;font-size:12px;line-height:17px;color:#555}
.product-btn{position:absolute;left:123px;top:104px;width:124px;height:30px;border-radius:3px;background:linear-gradient(#e8262f,#b10d15);color:#fff;font-size:11px;font-weight:700;display:flex;align-items:center;padding-left:8px;gap:14px}
.footer-copy{left:120px;top:1140px;font-size:12px;color:var(--blue)}
.footer-links{left:120px;top:1160px;font-size:12px;color:#444;word-spacing:2px}
.footer-addr{right:115px;top:1140px;font-size:12px;color:var(--blue);text-align:right}
.footer-mail{right:115px;top:1160px;font-size:12px;color:#444}
</style>
</head>
<body>
<div class="page">
  <div class="top-band"></div>

  <header>
    <div class="abs brand">
      <div class="brand-mark"></div>
      <div class="brand-name">Blaze Guard<br>Safety &amp; Solutions</div>
    </div>
    <div class="abs contact-link">
      <svg width="16" height="11" viewBox="0 0 16 11"><rect x=".5" y=".5" width="15" height="10" fill="#ddd" stroke="#999"/><path d="M.5 .5 8 6 15.5 .5" fill="none" stroke="#999"/></svg>
      Contact Us
    </div>
    <div class="abs search">
      <div class="search-field">
        <svg width="14" height="14" viewBox="0 0 14 14"><circle cx="5.5" cy="5.5" r="4.2" fill="none" stroke="#999" stroke-width="1.6"/><path d="M8.6 8.6 13 13" stroke="#999" stroke-width="1.8"/></svg>
        enter keyword
      </div>
      <div class="search-btn">Search</div>
    </div>
    <nav class="abs nav">
      <div class="nav-item active">Home</div>
      <div class="nav-item">Products</div>
      <div class="nav-item">Services</div>
      <div class="nav-item">Technical Information <svg width="9" height="5"><path d="M0 0h9L4.5 5z" fill="#ddd"/></svg></div>
      <div class="nav-item">Company Information <svg width="9" height="5"><path d="M0 0h9L4.5 5z" fill="#ddd"/></svg></div>
      <div class="nav-phone">
        <svg width="17" height="17" viewBox="0 0 24 24"><path d="M6.6 10.8c1.4 2.8 3.8 5.1 6.6 6.6l2.2-2.2c.3-.3.7-.4 1-.2 1.1.4 2.300.6 3.6.6.6 0 1 .4 1 1V20c0 .6-.4 1-1 1C10.6 21 3 13.4 3 4c0-.6.4-1 1-1h3.5c.6 0 1 .4 1 1 0 1.3.2 2.5.6 3.6.1.3 0 .7-.2 1z" fill="#ccc"/></svg>
        (121) 555-0142
      </div>
    </nav>
  </header>

  <section>
    <div class="abs hero-frame"></div>
    <div class="abs hero" role="img" aria-label="Photo of firefighters in yellow gear tackling a large blaze"></div>
    <h1 class="abs hero-title">Fire, Safety</h1>
    <div class="abs hero-sub">&amp; First aid equipment</div>
    <p class="abs hero-lead"><span>Blaze Guard is a owner operated business so our reputation is our guarantee to do the best job we possibly can.</span></p>
    <div class="abs hero-btn">Browse products <svg width="9" height="10"><path d="M0 0l9 5-9 5z" fill="#fff"/></svg></div>
    <div class="abs thumbs">
      <div class="thumb" role="img" aria-label="Fire extinguisher thumbnail" style="background:linear-gradient(#eee,#c33)"></div>
      <div class="thumb" role="img" aria-label="Fire hose reel thumbnail" style="background:linear-gradient(#fff,#d42222)"></div>
      <div class="thumb" role="img" aria-label="Fire blanket thumbnail" style="background:linear-gradient(#e22,#b00)"></div>
      <div class="thumb" role="img" aria-label="Hard hat thumbnail" style="background:linear-gradient(#e6c93a,#3a4a3a)"></div>
    </div>
  </section>

  <section class="abs stats">
    <div class="stat">
      <div class="big-48">48</div>
      <div class="stat-title">Blaze Guard Safety &amp; Solutions</div>
      <div class="stat-note">Best Products</div>
    </div>
    <div class="stat">
      <div class="million">3 MILLION<small>FIRE EXTINGUISHERS SOLD</small></div>
      <div class="stat-title">Thousands of satisfied customers</div>
      <div class="stat-note">100% NSW Owned and Operated</div>
    </div>
    <div class="stat">
      <svg class="exit-sign" width="128" height="63" viewBox="0 0 128 63"><rect width="128" height="63" rx="2" fill="#1f9a3a"/><rect x="62" y="6" width="2" height="51" fill="#fff"/><path d="M74 27h22V17l18 14-18 14V35H74z" fill="#fff"/></svg>
      <div class="stat-title" style="top:96px">Emergency Services</div>
      <div class="stat-note" style="top:116px">24 hours a day, 7 days a week, nights and holidays included.</div>
    </div>
    <div class="stat">
      <div class="hand-truck" role="img" aria-label="Hand truck carrying a cardboard box"></div>
      <div class="stat-title">Ordering Made Easy</div>
      <div class="stat-note">Order by phone, fax or mail. Our sales staff will be happy to assist you</div>
    </div>
  </section>

  <main>
    <h2 class="abs welcome">Welcome to Blaze Guard Safety &amp; Solutions</h2>
    <p class="abs intro">your source for not only quality fire extinguishers, but fire alarms, emergency &amp; exit lighting,<br>respirators, hard hats, safety glasses, first aid products, eyewash stations&nbsp; and much, much more.</p>
    <div class="abs body-copy">
      <p>Blaze Guard is a fire protection company situated on the Central Coast of NSW and is currently servicing the Sydney, Central Coast and Hunter areas, We are always looking for new clients who are not happy with there current service providers and are looking for a Competitive priced alternative. Blaze Guard will come to your site and assess your fire service assets and provide a full quotation on a 12 month service contract.</p>
      <p>Blaze Guard can also supply quotations for any alterations to your Sprinklers,Hydrants &amp; Hose reel systems along with your fire detection and emergency lighting.</p>
      <p>Blaze Guard is a owner operated business, so our reputation is our guarantee to do the best job we possibly can.<br>We use only manufacturer recommended parts and U.L.C. listed chemicals for recharging your fire equipment.</p>
    </div>
    <div class="abs divider"></div>

    <aside>
      <div class="abs quote">
        <div class="quote-small">Get a Product</div>
        <div class="quote-big">QUOTE</div>
        <svg class="quote-bubble" width="104" height="84" viewBox="0 0 104 84"><path d="M12 4h84a5 5 0 0 1 5 5v46a5 5 0 0 1-5 5H48L30 81l5-21H12a5 5 0 0 1-5-5V9a5 5 0 0 1 5-5z" fill="none" stroke="#35c3ea" stroke-width="5"/></svg>
        <div class="quote-note">Our Quotation Generator will<br>allow you to add items to your cart and submit a NO OBLIGATION request for quotation!</div>
      </div>
      <div class="abs product">
        <div class="product-img" role="img" aria-label="Boxed product package"></div>
        <div class="product-title">Fire Hose Reels<br>and Hydrants</div>
        <div class="product-text">Lorem ipsum dolor sit amet, cons adipiscing elit.</div>
        <div class="product-btn">Request a quote <svg width="13" height="13"><circle cx="6.5" cy="6.5" r="6.5" fill="#7a0a0f"/><path d="M3.5 5h6L6.5 9z" fill="#fff"/></svg></div>
      </div>
    </aside>
  </main>

  <footer>
    <div class="abs footer-copy">Copyright 2011, blazeguard-example.com.au. All rights reserved.</div>
    <div class="abs footer-links">sitemap &nbsp;|&nbsp; contact &nbsp;|&nbsp; privacy policy</div>
    <div class="abs footer-addr">1323 – Harbour Rd, Gosford, NSW 2250</div>
    <div class="abs footer-mail">info@blazeguard-example.com.au</div>
  </footer>
</div>
</body>
</html>
```